Create New Bussiness Card For New Shoes Store

Vandrule is a store that sells a variety of skateboard shoes such as Kestro, Mollen etc. we also sell some skateboard and all skateboard accessories.
we like black and white style logo, but also like blue as well.
We are fully assembled with a deck, truck, wheels, and bearings. Add some personality to your board with a fun, graphic skateboard deck. Constructed of thick 7 ply maple,
Target Market(s)
Target audience: 12-40 year old
especially for young man
Industry/Entity Type
Industrial
Contact Information for Business Card
Name: Vandrule
Address1: 2483 Harlow Brisket Rd
City: Xenia
State: Ohio
Zip: 45385
Country: US
Phone: 614830296
email: markolvenby@plimmail.test

```html
<!DOCTYPE html>
<html lang="en">
<head>
<meta charset="utf-8">
<title>Vandrule Business Card</title>
<link rel="stylesheet" href="https://fonts.googleapis.com/css2?family=Arimo:wght@400&display=swap">
<style>
  :root {
    --backdrop: #8c8c8c;
    --card-black: #050505;
    --card-edge: #3a3a3a;
    --ink-white: #ffffff;
    --card-font: "Arimo", Arial, sans-serif;
  }
  * { box-sizing: border-box; margin: 0; padding: 0; }
  html, body {
    width: 1200px;
    height: 1000px;
    overflow: hidden;
  }
  body {
    position: relative;
    background: var(--backdrop);
    font-family: var(--card-font);
    color: var(--ink-white);
  }
  .business-card {
    position: absolute;
    left: 382px;
    width: 438px;
    height: 262px;
    background: var(--card-black);
    border-radius: 14px;
    box-shadow: 0 0 0 2px var(--card-edge);
  }
  .card-front { top: 152px; }
  .card-back { top: 567px; }
  .card-frame {
    position: absolute;
    inset: 7px;
    border: 1.5px solid var(--ink-white);
    border-radius: 12px;
  }

  /* Front */
  .front-wordmark {
    position: absolute;
    left: 0;
    right: 0;
    top: 102px;
    text-align: center;
    font-size: 44px;
    line-height: 52px;
    font-weight: 400;
    letter-spacing: 1px;
  }
  .front-email {
    position: absolute;
    left: 419px;
    top: 199px;
    font-size: 7px;
    line-height: 8px;
    white-space: nowrap;
    transform: translate(-50%, -50%) rotate(-90deg);
  }

  /* Back */
  .back-divider {
    position: absolute;
    left: 9px;
    right: 9px;
    top: 46px;
    height: 1.5px;
    background: var(--ink-white);
  }
  .back-wordmark {
    position: absolute;
    left: 50%;
    top: 36px;
    transform: translateX(-50%);
    padding: 0 8px;
    background: var(--card-black);
    font-size: 19px;
    line-height: 22px;
    font-weight: 400;
    white-space: nowrap;
  }
  .contact-discs {
    position: absolute;
    top: 101px;
    left: 27px;
    right: 27px;
    display: flex;
    justify-content: space-between;
  }
  .contact-disc {
    width: 122px;
    height: 122px;
    border: 2px solid var(--ink-white);
    border-radius: 50%;
    overflow: hidden;
    display: flex;
    flex-direction: column;
  }
  .disc-label {
    height: 27px;
    border-bottom: 1.5px solid var(--ink-white);
    display: flex;
    align-items: flex-end;
    justify-content: center;
    padding-bottom: 2px;
    font-size: 11px;
  }
  .disc-value {
    flex: 1;
    display: flex;
    align-items: flex-start;
    justify-content: center;
    text-align: center;
    font-size: 14px;
    line-height: 1.25;
    padding-top: 12px;
  }
  .disc-value.single-line { padding-top: 28px; }
</style>
</head>
<body>
  <section class="business-card card-front" aria-label="Card front">
    <div class="card-frame"></div>
    <div class="front-wordmark">Vandrule</div>
    <div class="front-email">markolvenby@plimmail.test</div>
  </section>

  <section class="business-card card-back" aria-label="Card back">
    <div class="card-frame"></div>
    <div class="back-divider"></div>
    <div class="back-wordmark">Vandrule</div>
    <div class="contact-discs">
      <div class="contact-disc">
        <div class="disc-label">Address 1</div>
        <div class="disc-value">2483,<br>Harlow,<br>Brisket Rd.</div>
      </div>
      <div class="contact-disc">
        <div class="disc-label">Address 2</div>
        <div class="disc-value">Corvale,<br>Brenmoor,<br>58210 US.</div>
      </div>
      <div class="contact-disc">
        <div class="disc-label">Phone</div>
        <div class="disc-value single-line">614830296</div>
      </div>
    </div>
  </section>
</body>
</html>
```